New homepage for a digital cleaning company

We are Kelmar Tidy Works. A company that provides other companies (mostly restaurants, hotels, gas stations) with cleaning products and a mobile app to register daily, weekly, monthly tasks that they have to complete in order to meet cleaning regulation in Europe. We now have a website www.kelmartidyworks.example. This website is not optimized for the right goals. We offer this service as a subscription. There are three subsciption types people can choose from. We would like a clean, modern and professional website that also functions as a webshop. Please consider recommending a wordpress theme, we are working with visual composer.
Our app is mostly used on tablets.
We have three subsciptions: 1 dashboard of 6 products = premium = 100 eur
1 dashboard of 4 products = professional = 90 eur
1 dashboard of 3 products = basic = 85 eur
We would like a homepage designed + product page + subsciption page + how it works page + functionalities of the app page. (if possible also the about us and contact page).
Target Market(s)
gas stations, restaurants, hotels,... All companies that have to deal with HACCP regulation of hygiene.
Industry/Entity Type
Cleaning Service
Number of Pages Required
3 page
Requirements
Nice to have
- Recommended wordpress theme

```html
<!DOCTYPE html>
<html lang="en">
<head>
<meta charset="utf-8">
<title>Kelmar Tidy Works – Digital Cleaning Service</title>
<link href="https://fonts.googleapis.com/css2?family=Montserrat:wght@600;700&family=Mulish:wght@400;600;700&display=swap" rel="stylesheet">
<style>
:root{
  --blue:#2f9cf4;
  --blue-dark:#1d86de;
  --navy:#101b2b;
  --ink:#222a36;
  --muted:#7a8494;
  --line:#e3e8ef;
  --paper:#ffffff;
  --tick:#8a94a2;
}
*{box-sizing:border-box;margin:0;padding:0}
html,body{width:1200px;height:2848px;overflow:hidden}
body{position:relative;background:var(--paper);font-family:"Mulish",sans-serif;color:var(--ink)}
.abs{position:absolute}
h1,h2,h3{font-family:"Montserrat",sans-serif}

/* hero */
.hero-wave{left:0;top:0;width:1200px;height:760px}
.brand{left:60px;top:30px;color:#fff;font:700 24px "Montserrat",sans-serif;display:flex;align-items:center;gap:10px}
.brand .dot{width:14px;height:14px;background:#fff;border-radius:50%}
.nav{right:70px;top:38px;display:flex;gap:30px;list-style:none}
.nav a{color:#fff;text-decoration:none;font-size:15px;font-weight:600}
.phone-art{left:200px;top:110px;width:330px;height:560px;border-radius:44px;transform:rotate(-14deg);background:linear-gradient(160deg,#3a4452,#161c25);box-shadow:0 30px 50px rgba(0,0,0,.25)}
.phone-art::after{content:"";position:absolute;inset:46px 20px;border-radius:14px;background:linear-gradient(180deg,#e9f5ff,#bfe2ff)}
.hero-title{left:690px;top:280px;width:460px;color:#fff;font-size:40px;line-height:1.22;text-align:right}
.hero-text{left:700px;top:400px;width:450px;color:#e6f3ff;font-size:15px;line-height:1.6;text-align:right}
.hero-actions{right:50px;top:494px;display:flex;gap:26px}
.btn-light{background:#fff;color:var(--blue);border-radius:4px;padding:14px 34px;font-weight:700;font-size:15px}
.mascot{border-radius:50%;background:radial-gradient(circle at 45% 40%,#e9c9a0,#c9935e 70%,#9e6c3f)}
.mascot-hero{left:570px;top:600px;width:140px;height:160px}

/* keys section */
.keys-tabs{left:70px;top:830px;width:260px;list-style:none;text-align:right}
.keys-tabs li{padding:20px 22px;font-weight:700;font-size:15px;color:#505a68;border-right:3px solid var(--line);white-space:nowrap}
.keys-tabs li.active{background:var(--blue);color:#fff;border-right-color:var(--blue-dark)}
.keys-body{left:370px;top:830px;width:330px}
.keys-body h3{color:var(--blue);font-size:17px;margin-bottom:10px}
.keys-body p{font-size:14px;line-height:1.65;color:#5a6474;margin-bottom:22px}
.btn-blue{display:inline-block;background:var(--blue);color:#fff;border-radius:4px;padding:14px 36px;font-weight:700;font-size:15px}
.tablet-art{left:760px;top:780px;width:400px;height:420px;background:linear-gradient(140deg,#dff0ff,#5cb4f7);border-radius:30px;transform:skewY(-6deg)}
.divider{left:0;top:1300px;width:1200px;height:1px;background:var(--line)}

/* services */
.services-title{left:0;top:1330px;width:1200px;text-align:center}
.services-title h2{color:var(--blue);font-size:40px}
.services-title p{font-size:14px;color:var(--muted);margin-top:8px}
.mascot-services{left:40px;top:1316px;width:110px;height:124px}
.plan{top:1450px;width:260px;height:560px;background:#fff;border-radius:8px;box-shadow:0 10px 34px rgba(20,40,80,.12);text-align:center;padding:30px 24px}
.plan h3{font-size:26px;font-weight:600}
.plan .price{color:var(--blue);font-size:44px;font-weight:600;font-family:"Montserrat",sans-serif;padding-bottom:18px;border-bottom:1px solid var(--line)}
.plan ul{list-style:none;text-align:left;margin-top:20px}
.plan li{display:flex;align-items:center;gap:10px;font-size:13px;color:#6a7482;margin-bottom:12px;white-space:nowrap}
.plan li svg{flex:none}
.product-art{width:80px;height:160px;margin:10px auto 20px;background:linear-gradient(180deg,#2b2f36,#0d1015);border-radius:4px}
.plan .btn-blue{padding:11px 30px;font-size:14px}

/* contact */
.contact-heading{left:0;top:2090px;width:1200px;text-align:center;font-size:44px;color:var(--ink)}
.mascot-contact{left:960px;top:2030px;width:120px;height:150px}
.footer-band{left:0;top:2420px;width:1200px;height:428px;background:var(--blue)}
.contact-card{left:80px;top:2190px;width:580px;height:370px;background:var(--navy);padding:60px 60px;color:#fff}
.contact-card h2{font-size:34px;margin-bottom:30px}
.contact-card .item{display:flex;gap:18px;align-items:flex-start;font-size:17px;line-height:1.5;margin-bottom:18px}
.form-card{left:620px;top:2240px;width:500px;height:330px;background:#fff;padding:36px 40px;box-shadow:0 10px 30px rgba(20,40,80,.15)}
.form-card h2{color:var(--blue);font-size:30px;margin-bottom:22px}
.row{display:flex;gap:18px;margin-bottom:14px}
.field{flex:1;height:36px;border:1px solid #cfd6df;border-radius:3px;font-size:12px;color:var(--muted);padding:10px 12px}
.field.msg{height:64px}
.form-card .btn-blue{padding:10px 28px;font-size:13px}
.social{left:0;top:2690px;width:1200px;display:flex;justify-content:center;gap:14px}
.social span{width:26px;height:26px;border-radius:50%;background:#fff}
.legal{left:0;top:2740px;width:1200px;text-align:center;color:#fff;font-size:14px}
</style>
</head>
<body>

<svg class="abs hero-wave" viewBox="0 0 1200 760" aria-hidden="true">
  <path d="M0 0H1200V560C1080 600 1000 540 860 600C720 660 640 700 480 690C300 680 160 700 0 740Z" fill="var(--blue)"/>
</svg>

<div class="abs brand"><span class="dot"></span>Kelmar Tidy Works</div>
<ul class="abs nav">
  <li><a href="#">Home</a></li><li><a href="#">About Us</a></li><li><a href="#">Prices</a></li>
  <li><a href="#">Contact</a></li><li><a href="#">Faq</a></li><li><a href="#">Online Store</a></li><li><a href="#">Themes</a></li>
</ul>

<div class="abs phone-art" role="img" aria-label="Smartphone showing the cleaning task app"></div>
<h1 class="abs hero-title">Haccp Paperworkls a Thing Of The Past</h1>
<p class="abs hero-text">Kelmar Tidy Works is a service in the form of monthly contracts, which originated from the needs of companies that want to clean and maintain more efficiently.</p>
<div class="abs hero-actions"><span class="btn-light">Contact Us</span><span class="btn-light">Request an Offer</span></div>
<div class="abs mascot mascot-hero" role="img" aria-label="Cartoon mascot character waving"></div>

<ul class="abs keys-tabs">
  <li>No More Paperwork</li>
  <li>Happy Customers</li>
  <li>Doing Business Honestly</li>
  <li class="active">Safe &amp; Hygienic</li>
</ul>
<div class="abs keys-body">
  <h3>The 3 Keys To Success</h3>
  <p>From Physical Safety To Sensor Safety, Customer-oriented Working In A Clean And Safe Environment.</p>
  <h3>For the employees:</h3>
  <p>Clear daily tasks that help you welcome your customers, save them time and make every visit as pleasant as possible.</p>
  <span class="btn-blue">Read More</span>
</div>
<div class="abs tablet-art" role="img" aria-label="Tablet screens of the app dashboard with charts"></div>
<div class="abs divider"></div>

<div class="abs mascot mascot-services" role="img" aria-label="Cartoon mascot character with a speech bubble"></div>
<div class="abs services-title"><h2>We Offer Service</h2><p>We got something for everyone</p></div>

<div class="abs plan" style="left:170px">
  <h3>Basic</h3><div class="price">85 eur</div>
  <ul>
    <li><svg width="14" height="14" viewBox="0 0 14 14"><circle cx="7" cy="7" r="7" fill="var(--tick)"/><path d="M4 7.2l2 2 4-4" stroke="#fff" stroke-width="1.6" fill="none"/></svg>Lorem ipsum dolor sit amet</li>
    <li><svg width="14" height="14" viewBox="0 0 14 14"><circle cx="7" cy="7" r="7" fill="var(--tick)"/><path d="M4 7.2l2 2 4-4" stroke="#fff" stroke-width="1.6" fill="none"/></svg>Lorem ipsum dolor sit amet</li>
    <li><svg width="14" height="14" viewBox="0 0 14 14"><circle cx="7" cy="7" r="7" fill="var(--tick)"/><path d="M4 7.2l2 2 4-4" stroke="#fff" stroke-width="1.6" fill="none"/></svg>Lorem ipsum dolor sit amet</li>
    <li><svg width="14" height="14" viewBox="0 0 14 14"><circle cx="7" cy="7" r="7" fill="var(--tick)"/><path d="M4 7.2l2 2 4-4" stroke="#fff" stroke-width="1.6" fill="none"/></svg>Lorem ipsum dolor sit amet</li>
    <li><svg width="14" height="14" viewBox="0 0 14 14"><circle cx="7" cy="7" r="7" fill="var(--tick)"/><path d="M4 7.2l2 2 4-4" stroke="#fff" stroke-width="1.6" fill="none"/></svg>Lorem ipsum dolor sit amet</li>
  </ul>
  <div class="product-art" role="img" aria-label="Product dashboard with three cleaning products"></div>
  <span class="btn-blue">Subscribe</span>
</div>

<div class="abs plan" style="left:470px">
  <h3>Professional</h3><div class="price">90 eur</div>
  <ul>
    <li><svg width="14" height="14" viewBox="0 0 14 14"><circle cx="7" cy="7" r="7" fill="var(--tick)"/><path d="M4 7.2l2 2 4-4" stroke="#fff" stroke-width="1.6" fill="none"/></svg>Lorem ipsum dolor sit amet</li>
    <li><svg width="14" height="14" viewBox="0 0 14 14"><circle cx="7" cy="7" r="7" fill="var(--tick)"/><path d="M4 7.2l2 2 4-4" stroke="#fff" stroke-width="1.6" fill="none"/></svg>Lorem ipsum dolor sit amet</li>
    <li><svg width="14" height="14" viewBox="0 0 14 14"><circle cx="7" cy="7" r="7" fill="var(--tick)"/><path d="M4 7.2l2 2 4-4" stroke="#fff" stroke-width="1.6" fill="none"/></svg>Lorem ipsum dolor sit amet</li>
    <li><svg width="14" height="14" viewBox="0 0 14 14"><circle cx="7" cy="7" r="7" fill="var(--tick)"/><path d="M4 7.2l2 2 4-4" stroke="#fff" stroke-width="1.6" fill="none"/></svg>Lorem ipsum dolor sit amet</li>
    <li><svg width="14" height="14" viewBox="0 0 14 14"><circle cx="7" cy="7" r="7" fill="var(--tick)"/><path d="M4 7.2l2 2 4-4" stroke="#fff" stroke-width="1.6" fill="none"/></svg>Lorem ipsum dolor sit amet</li>
  </ul>
  <div class="product-art" role="img" aria-label="Product dashboard with four cleaning products"></div>
  <span class="btn-blue">Subscribe</span>
</div>

<div class="abs plan" style="left:770px">
  <h3>Premium</h3><div class="price">100 eur</div>
  <ul>
    <li><svg width="14" height="14" viewBox="0 0 14 14"><circle cx="7" cy="7" r="7" fill="var(--tick)"/><path d="M4 7.2l2 2 4-4" stroke="#fff" stroke-width="1.6" fill="none"/></svg>Lorem ipsum dolor sit amet</li>
    <li><svg width="14" height="14" viewBox="0 0 14 14"><circle cx="7" cy="7" r="7" fill="var(--tick)"/><path d="M4 7.2l2 2 4-4" stroke="#fff" stroke-width="1.6" fill="none"/></svg>Lorem ipsum dolor sit amet</li>
    <li><svg width="14" height="14" viewBox="0 0 14 14"><circle cx="7" cy="7" r="7" fill="var(--tick)"/><path d="M4 7.2l2 2 4-4" stroke="#fff" stroke-width="1.6" fill="none"/></svg>Lorem ipsum dolor sit amet</li>
    <li><svg width="14" height="14" viewBox="0 0 14 14"><circle cx="7" cy="7" r="7" fill="var(--tick)"/><path d="M4 7.2l2 2 4-4" stroke="#fff" stroke-width="1.6" fill="none"/></svg>Lorem ipsum dolor sit amet</li>
    <li><svg width="14" height="14" viewBox="0 0 14 14"><circle cx="7" cy="7" r="7" fill="var(--tick)"/><path d="M4 7.2l2 2 4-4" stroke="#fff" stroke-width="1.6" fill="none"/></svg>Lorem ipsum dolor sit amet</li>
  </ul>
  <div class="product-art" role="img" aria-label="Product dashboard with six cleaning products"></div>
  <span class="btn-blue">Subscribe</span>
</div>

<div class="abs mascot mascot-contact" role="img" aria-label="Cartoon mascot character holding a phone"></div>
<h2 class="abs contact-heading">Contact Us</h2>

<div class="abs footer-band"></div>

<div class="abs contact-card">
  <h2>Contact Us</h2>
  <div class="item"><svg width="20" height="22" viewBox="0 0 20 22"><path d="M10 1a7 7 0 0 0-7 7c0 5 7 13 7 13s7-8 7-13a7 7 0 0 0-7-7z" fill="#fff"/><circle cx="10" cy="8" r="2.6" fill="var(--navy)"/></svg><span>Lindenkade 48,<br>5211 KT Brammel, NL</span></div>
  <div class="item"><svg width="20" height="20" viewBox="0 0 20 20"><path d="M4 2l3 0 2 5-2 1.5c1 2.3 2.7 4 5 5L13.5 11l5 2v3c0 1-1 2-2 2C9 18 2 11 2 4c0-1 1-2 2-2z" fill="#fff"/></svg><span>+31 100 22 45 00</span></div>
  <div class="item"><svg width="20" height="20" viewBox="0 0 20 20"><path d="M4 2l3 0 2 5-2 1.5c1 2.3 2.7 4 5 5L13.5 11l5 2v3c0 1-1 2-2 2C9 18 2 11 2 4c0-1 1-2 2-2z" fill="#fff"/></svg><span>+31 600 48 27 31</span></div>
  <div class="item"><svg width="22" height="18" viewBox="0 0 22 18"><rect x="1" y="2" width="20" height="14" rx="2" fill="#fff"/><path d="M2 3l9 7 9-7" stroke="var(--navy)" stroke-width="1.6" fill="none"/></svg><span>hello@kelmartidyworks.example</span></div>
</div>

<form class="abs form-card">
  <h2>Get In Touch</h2>
  <div class="row"><div class="field">Name</div><div class="field">Email</div></div>
  <div class="row"><div class="field">Phone Number</div><div class="field">Subject</div></div>
  <div class="row"><div class="field msg">Message</div></div>
  <span class="btn-blue">Submit</span>
</form>

<div class="abs social"><span></span><span></span><span></span><span></span></div>
<p class="abs legal">© 2018 Copyrights | All Rights Reserved | Terms &amp; Conditions | Privacy Policy</p>

</body>
</html>
```